Vellorine Baby Collection

We are creating the label for baby skin care products for our existing skin care brand called Vellorine. we want to play on sophistication of Vellorine current labelling and change to include kids/baby look and feel but keeping the up market style. We will have full range of different products like
1.Shampoo and Body Wash
2. Healing Cream
3. Nappy Rush Cream
4. Baby Massage Gel
5.Baby Bubble Bath
6.Baby Soothing Skin Lotion

Target Market(s)

Our target market are customers in Australia and Asia looking to purchase quality skin care products for their new born babies and young children

Industry/Entity Type

Skin care

Requirements
Must have
• some children look combined with an existing Vellorine brand
Nice to have
• maybe some baby toys and letters around the main name Vellorine

```html
<!DOCTYPE html>
<html lang="en">
<head>
<meta charset="utf-8">
<title>Vellorine Body Wash Label</title>
<link rel="stylesheet" href="https://fonts.googleapis.com/css2?family=Libre+Baskerville:wght@700&family=Fredoka:wght@600&family=Roboto:wght@400&display=swap">
<style>
  :root {
    --canvas-bg: #f1f1f1;
    --label-bg: #e7e7e7;
    --ink: #1d1d1d;
    --ink-soft: #3a3a3a;
    --dot-blue: #a9d2e2;
    --dot-pink: #efb3c3;
    --dot-beige: #f0dcc4;
    --dot-dark: #141414;
    --arc-pink: #eab0c6;
    --letter-1: #e8479a;
    --letter-2: #d54ea6;
    --letter-3: #b160b0;
    --letter-4: #9a68b5;
    --letter-5: #6f78bd;
    --letter-6: #4f86c3;
    --letter-7: #3b8fc6;
    --letter-8: #2d95c8;
  }
  * { margin: 0; padding: 0; box-sizing: border-box; }
  html, body {
    width: 1200px;
    height: 1200px;
    overflow: hidden;
    background: var(--canvas-bg);
  }
  .canvas {
    position: relative;
    width: 1200px;
    height: 1200px;
  }
  .label {
    position: absolute;
    left: 245px;
    top: 72px;
    width: 710px;
    height: 1056px;
    background: var(--label-bg);
    overflow: hidden;
  }
  .label-shapes {
    position: absolute;
    inset: 0;
    width: 710px;
    height: 1056px;
  }
  .brand-name {
    position: absolute;
    top: 222px;
    left: 0;
    width: 100%;
    text-align: center;
    font-family: "Libre Baskerville", serif;
    font-weight: 700;
    font-size: 44px;
    letter-spacing: 1px;
    color: var(--ink);
  }
  .product-name {
    position: absolute;
    top: 462px;
    left: 0;
    width: 100%;
    text-align: center;
    font-family: "Fredoka", sans-serif;
    font-weight: 600;
    font-size: 104px;
    line-height: 1;
    white-space: nowrap;
  }
  .product-name .word + .word { margin-left: 34px; }
  .l1 { color: var(--letter-1); }
  .l2 { color: var(--letter-2); }
  .l3 { color: var(--letter-3); }
  .l4 { color: var(--letter-4); }
  .l5 { color: var(--letter-5); }
  .l6 { color: var(--letter-6); }
  .l7 { color: var(--letter-7); }
  .l8 { color: var(--letter-8); }
  .product-description {
    position: absolute;
    top: 660px;
    left: 0;
    width: 100%;
    text-align: center;
    font-family: "Roboto", sans-serif;
    font-size: 28px;
    line-height: 42px;
    letter-spacing: -0.5px;
    color: var(--ink-soft);
  }
  .product-usage {
    position: absolute;
    top: 790px;
    left: 0;
    width: 100%;
    text-align: center;
    font-family: "Roboto", sans-serif;
    font-size: 31px;
    color: var(--ink);
  }
</style>
</head>
<body>
  <main class="canvas">
    <section class="label">
      <svg class="label-shapes" viewBox="0 0 710 1056" aria-hidden="true">
        <circle class="dot-edge-dark" cx="0" cy="256" r="20" fill="var(--dot-dark)"/>
        <circle class="dot-edge-beige" cx="6" cy="704" r="15" fill="var(--dot-beige)"/>
        <circle class="dot-blue" cx="294" cy="358" r="33" fill="var(--dot-blue)"/>
        <circle class="dot-pink" cx="405" cy="390" r="42" fill="var(--dot-pink)"/>
        <circle class="dot-beige" cx="272" cy="446" r="18" fill="var(--dot-beige)"/>
        <circle class="arc-pink" cx="705" cy="885" r="100" fill="var(--arc-pink)"/>
        <circle class="dot-blue-corner" cx="670" cy="785" r="33" fill="var(--dot-blue)" opacity="0.85"/>
      </svg>

      <h1 class="brand-name">Vellorine</h1>

      <h2 class="product-name">
        <span class="word"><span class="l1">B</span><span class="l2">o</span><span class="l3">d</span><span class="l4">y</span></span><span class="word"><span class="l5">W</span><span class="l6">a</span><span class="l7">s</span><span class="l8">h</span></span>
      </h2>

      <p class="product-description">Vellorine Herbal Nourishing<br>Collagen &amp; 7 in 1 essential oils</p>

      <p class="product-usage">FOR EVERYDAY USE · 500ml</p>
    </section>
  </main>
</body>
</html>
```